Personal Injury Law Firm Marketing Postcards

Looking for 4 different high quality graphic postcards (print on both sides of 4"x6" postcard to market a Personal Injury Lawyer (Walter Dunmore). These will be placed on cars and in stores on stands. My photo and/or stock images.... We are targeting People who have been injured in automobile accidents, motorcycle accidents, slip and fall (wet/greasy floors indoors in supermarkets, restaurants, etc., snow and ice outdoors on sidewalks) trip and fall cases on dangerous staircases. indoor/outdoor, dog bite injuries. ( I like the use of stock images of these type of injury causing accidents. You can use following language "Serving People Injured in NY & NJ" . Millions of Dollars Recovered, Free Consultation and No Fee Unless We Recover Money! Phone number to be displayed (555) 614-3082 "call or text" Available 24 hours a day 7 days per week. May also want to mention that we can take over your case from another lawyer if you are not satisfied with your current attorney. There should be a small space in corner which has a space for my marketing person to handwrite in their reference code.

Target Market(s)

18-75 years old - densely populated major city

Industry/Entity Type

Legal

Font styles to use
Other font styles liked:
• Please use logo style that I uploaded.. Please do not just cut parts of my website out and use them. Do not use LOGO from my website

Colors
0054AA
0677BA
7BADD7
CADEEF
E8F1F8
00AB8E
00BBA5
67D7C9
C6EFE9
E9F9F6

Requirements
Must have
• Professional Appearance

```html
<!DOCTYPE html>
<html lang="en">
<head>
<meta charset="utf-8">
<title>Walter Dunmore P.C. – Personal Injury Postcards</title>
<link href="https://fonts.googleapis.com/css2?family=Montserrat:wght@400;500;600;700;800&display=swap" rel="stylesheet">
<style>
:root{
  --navy:#1b2f5e;
  --navy-deep:#14234a;
  --blue:#1f5aa5;
  --blue-mid:#2f6fb8;
  --blue-light:#7badd7;
  --gold:#c9a45c;
  --gold-light:#e0c58f;
  --paper:#ffffff;
  --ink:#1d2433;
  --grey:#8a93a3;
  --stage:#ffffff;
}
*{box-sizing:border-box;margin:0;padding:0}
html,body{width:1200px;height:3876px;overflow:hidden;background:var(--stage);font-family:"Montserrat",Arial,sans-serif;color:var(--ink)}
.board{position:relative;width:1200px;height:3876px}
.set{position:absolute;left:0;width:1200px}
.set-staged{height:800px}
.set-flat{height:340px}
.set-staged .card{transform:scale(1.3);transform-origin:top left}
.card{position:absolute;width:510px;height:340px;overflow:hidden;background:var(--paper);box-shadow:0 8px 22px rgba(20,35,74,.22)}
.photo{position:absolute}
.abs{position:absolute}
.headline{font-weight:800;text-transform:uppercase;line-height:1.02;letter-spacing:.2px}
.small{font-size:6.5px;line-height:1.45}
.logo{display:flex;align-items:center;gap:5px;font-weight:700;font-size:9px;color:var(--navy)}
.logo-mark{width:12px;height:12px;background:var(--gold)}
.phone{display:flex;align-items:center;gap:4px;font-weight:700;font-size:9px}
.phone svg{width:10px;height:10px}
.offer{font-weight:700;line-height:1.2}
.tab{background:var(--gold);color:var(--navy);font-weight:800;font-size:11px;line-height:1.15;text-transform:uppercase;padding:8px 12px}
.areas-title{font-weight:800;font-size:10px;text-transform:uppercase;margin-bottom:6px}
.areas{list-style:none;font-size:7px;line-height:1.75}
.areas li{display:flex;align-items:center;gap:5px}
.areas li::before{content:"";width:4px;height:4px;background:var(--gold);flex:none}
.post-lines span{display:block;height:1px;background:currentColor;opacity:.55;margin-bottom:18px}
.stamp{position:absolute;width:40px;height:46px;border:1px dashed currentColor;opacity:.7}
.contact-row{display:flex;align-items:center;gap:5px;font-size:7px;margin-bottom:6px}
.contact-row svg{width:9px;height:9px;flex:none}
.ref-box{position:absolute;width:62px;height:22px;border:1px solid currentColor;opacity:.6}
</style>
</head>
<body>
<div class="board">

<!-- ===== Design 1 – staged pair ===== -->
<section class="set set-staged" style="top:20px">
  <article class="card back-one" style="left:130px;top:20px">
    <div class="photo" role="img" aria-label="Injured cyclist sitting on the road beside a car" style="left:0;top:0;width:205px;height:340px;background:linear-gradient(160deg,#c9c2b6,#8c8275 55%,#5c5650)"></div>
    <div class="abs" style="left:205px;top:0;width:305px;height:340px;background:linear-gradient(180deg,var(--navy) 0%,var(--blue) 100%)"></div>
    <div class="abs tab" style="left:205px;top:22px;width:220px">Law Office of Walter Dunmore P.C.<br>New York</div>
    <div class="abs" style="left:222px;top:92px;color:#fff">
      <div class="areas-title">Practice Areas</div>
      <ul class="areas"><li>Car Accidents</li><li>Motorcycle Accidents</li><li>Slip and Fall</li><li>Trip and Fall</li><li>Dog Bite Injuries</li><li>Pedestrian Accidents</li><li>Construction Injuries</li><li>Premises Liability</li></ul>
    </div>
    <div class="abs" style="left:370px;top:100px;width:120px;color:#fff">
      <div class="contact-row"><svg viewBox="0 0 24 24" fill="#fff"><path d="M12 2a7 7 0 0 0-7 7c0 5 7 13 7 13s7-8 7-13a7 7 0 0 0-7-7zm0 9.5A2.5 2.5 0 1 1 12 6a2.5 2.5 0 0 1 0 5.5z"/></svg>Law Office of Walter Dunmore P.C.</div>
      <div class="contact-row"><svg viewBox="0 0 24 24" fill="#fff"><path d="M6.6 10.8a15 15 0 0 0 6.6 6.6l2.2-2.2a1 1 0 0 1 1-.25 11.4 11.4 0 0 0 3.6.57 1 1 0 0 1 1 1V20a1 1 0 0 1-1 1A17 17 0 0 1 3 4a1 1 0 0 1 1-1h3.5a1 1 0 0 1 1 1c0 1.25.2 2.45.57 3.57a1 1 0 0 1-.25 1z"/></svg>(555) 614-3082</div>
    </div>
    <div class="abs" style="left:222px;top:306px;color:#fff;font-size:7px;font-weight:600">www.dunmorelaw.com</div>
    <div class="ref-box" style="left:432px;top:300px;color:#fff"></div>
  </article>
  <article class="card front-one" style="left:400px;top:300px">
    <div class="photo" role="img" aria-label="Lady Justice statue beside an attorney in a navy suit" style="left:0;top:0;width:510px;height:250px;background:linear-gradient(90deg,#a88a63 0%,#d8d2c2 30%,#eceae2 55%,#7f8a9c 78%,#3c4a66 100%)"></div>
    <div class="abs headline" style="left:172px;top:38px;width:170px;font-size:21px;color:var(--navy)">Serving People Injured in NY &amp; NJ</div>
    <p class="abs small" style="left:172px;top:130px;width:150px;color:var(--ink)">If you were injured in an accident, call us today for a free case review.</p>
    <div class="abs" style="left:0;top:250px;width:130px;height:90px;background:#fff"></div>
    <div class="abs logo" style="left:16px;top:286px"><span class="logo-mark"></span>Dunmore Law</div>
    <div class="abs" style="left:130px;top:250px;width:380px;height:90px;background:var(--navy)"></div>
    <div class="abs" style="left:130px;top:250px;width:6px;height:90px;background:var(--gold)"></div>
    <div class="abs offer" style="left:150px;top:270px;width:210px;font-size:13px;color:#fff">Free Consultation and<br>No Fee Unless We Recover Money</div>
    <div class="abs phone" style="left:382px;top:286px;color:#fff"><svg viewBox="0 0 24 24" fill="var(--gold)"><path d="M6.6 10.8a15 15 0 0 0 6.6 6.6l2.2-2.2a1 1 0 0 1 1-.25 11.4 11.4 0 0 0 3.6.57 1 1 0 0 1 1 1V20a1 1 0 0 1-1 1A17 17 0 0 1 3 4a1 1 0 0 1 1-1h3.5a1 1 0 0 1 1 1c0 1.25.2 2.45.57 3.57a1 1 0 0 1-.25 1z"/></svg>(555) 614-3082</div>
  </article>
</section>

<!-- ===== Design 1 – flat pair ===== -->
<section class="set set-flat" style="top:920px">
  <article class="card front-one" style="left:80px;top:0">
    <div class="photo" role="img" aria-label="Lady Justice statue beside an attorney in a navy suit" style="left:0;top:0;width:510px;height:250px;background:linear-gradient(90deg,#a88a63 0%,#d8d2c2 30%,#eceae2 55%,#7f8a9c 78%,#3c4a66 100%)"></div>
    <div class="abs headline" style="left:172px;top:38px;width:170px;font-size:21px;color:var(--navy)">Serving People Injured in NY &amp; NJ</div>
    <p class="abs small" style="left:172px;top:130px;width:150px">If you were injured in an accident, call us today for a free case review.</p>
    <div class="abs" style="left:0;top:250px;width:130px;height:90px;background:#fff"></div>
    <div class="abs logo" style="left:16px;top:286px"><span class="logo-mark"></span>Dunmore Law</div>
    <div class="abs" style="left:130px;top:250px;width:380px;height:90px;background:var(--navy)"></div>
    <div class="abs" style="left:130px;top:250px;width:6px;height:90px;background:var(--gold)"></div>
    <div class="abs offer" style="left:150px;top:270px;width:210px;font-size:13px;color:#fff">Free Consultation and<br>No Fee Unless We Recover Money</div>
    <div class="abs phone" style="left:382px;top:286px;color:#fff"><svg viewBox="0 0 24 24" fill="var(--gold)"><path d="M6.6 10.8a15 15 0 0 0 6.6 6.6l2.2-2.2a1 1 0 0 1 1-.25 11.4 11.4 0 0 0 3.6.57 1 1 0 0 1 1 1V20a1 1 0 0 1-1 1A17 17 0 0 1 3 4a1 1 0 0 1 1-1h3.5a1 1 0 0 1 1 1c0 1.25.2 2.45.57 3.57a1 1 0 0 1-.25 1z"/></svg>(555) 614-3082</div>
  </article>
  <article class="card back-one" style="left:610px;top:0">
    <div class="photo" role="img" aria-label="Injured cyclist sitting on the road beside a car" style="left:0;top:0;width:205px;height:340px;background:linear-gradient(160deg,#c9c2b6,#8c8275 55%,#5c5650)"></div>
    <div class="abs" style="left:205px;top:0;width:305px;height:340px;background:linear-gradient(180deg,var(--navy) 0%,var(--blue) 100%)"></div>
    <div class="abs tab" style="left:205px;top:22px;width:220px">Law Office of Walter Dunmore P.C.<br>New York</div>
    <div class="abs" style="left:222px;top:92px;color:#fff">
      <div class="areas-title">Practice Areas</div>
      <ul class="areas"><li>Car Accidents</li><li>Motorcycle Accidents</li><li>Slip and Fall</li><li>Trip and Fall</li><li>Dog Bite Injuries</li><li>Pedestrian Accidents</li><li>Construction Injuries</li><li>Premises Liability</li></ul>
    </div>
    <div class="abs" style="left:370px;top:100px;width:120px;color:#fff">
      <div class="contact-row"><svg viewBox="0 0 24 24" fill="#fff"><path d="M12 2a7 7 0 0 0-7 7c0 5 7 13 7 13s7-8 7-13a7 7 0 0 0-7-7zm0 9.5A2.5 2.5 0 1 1 12 6a2.5 2.5 0 0 1 0 5.5z"/></svg>Law Office of Walter Dunmore P.C.</div>
      <div class="contact-row"><svg viewBox="0 0 24 24" fill="#fff"><path d="M6.6 10.8a15 15 0 0 0 6.6 6.6l2.2-2.2a1 1 0 0 1 1-.25 11.4 11.4 0 0 0 3.6.57 1 1 0 0 1 1 1V20a1 1 0 0 1-1 1A17 17 0 0 1 3 4a1 1 0 0 1 1-1h3.5a1 1 0 0 1 1 1c0 1.25.2 2.45.57 3.57a1 1 0 0 1-.25 1z"/></svg>(555) 614-3082</div>
    </div>
    <div class="abs" style="left:222px;top:306px;color:#fff;font-size:7px;font-weight:600">www.dunmorelaw.com</div>
    <div class="ref-box" style="left:432px;top:300px;color:#fff"></div>
  </article>
</section>

<!-- ===== Design 2 – staged pair ===== -->
<section class="set set-staged" style="top:1340px">
  <article class="card back-two" style="left:130px;top:20px">
    <div class="photo" role="img" aria-label="Courthouse columns with a navy overlay" style="left:0;top:0;width:230px;height:340px;background:linear-gradient(180deg,#3b5c93 0%,#8da0bf 45%,#5d6f8e 100%)"></div>
    <div class="abs" style="left:0;top:0;width:230px;height:340px;background:linear-gradient(180deg,rgba(27,47,94,.85),rgba(27,47,94,.15) 55%,rgba(27,47,94,.05))"></div>
    <div class="abs" style="left:22px;top:50px;color:#fff">
      <div class="areas-title">Practice Areas</div>
      <ul class="areas"><li>Car Accidents</li><li>Motorcycle Accidents</li><li>Slip and Fall</li><li>Trip and Fall</li><li>Dog Bite Injuries</li><li>Pedestrian Accidents</li></ul>
    </div>
    <div class="abs" style="left:230px;top:0;width:280px;height:340px;background:linear-gradient(180deg,var(--blue-mid),var(--navy))"></div>
    <div class="abs tab" style="left:250px;top:22px;width:210px">Law Office of Walter Dunmore P.C.<br>New York</div>
    <div class="abs post-lines" style="left:260px;top:150px;width:220px;color:#fff"><span></span><span></span><span></span><span></span></div>
    <div class="ref-box" style="left:420px;top:300px;color:#fff"></div>
  </article>
  <article class="card front-two" style="left:400px;top:300px">
    <div class="photo" role="img" aria-label="Attorney in a navy suit in front of an American flag" style="left:0;top:0;width:230px;height:340px;background:linear-gradient(120deg,#2a3f73 0%,#b73a3a 28%,#e9e6e2 45%,#4a5a78 70%,#1f2d4f 100%)"></div>
    <div class="abs" style="left:230px;top:0;width:280px;height:150px;background:var(--gold)"></div>
    <div class="abs headline" style="left:250px;top:28px;width:240px;font-size:22px;color:#fff">Serving People Injured in NY &amp; NJ</div>
    <div class="abs" style="left:230px;top:150px;width:280px;height:90px;background:#fff"></div>
    <div class="abs offer" style="left:250px;top:172px;width:240px;font-size:14px;color:var(--navy)">Free Consultation and<br>No Fee Unless We Recover Money</div>
    <div class="abs" style="left:230px;top:240px;width:280px;height:100px;background:var(--navy)"></div>
    <p class="abs small" style="left:250px;top:262px;width:140px;color:#fff">If you were injured in an accident, call us today for a free case review.</p>
    <div class="abs phone" style="left:402px;top:266px;color:#fff"><svg viewBox="0 0 24 24" fill="var(--gold)"><path d="M6.6 10.8a15 15 0 0 0 6.6 6.6l2.2-2.2a1 1 0 0 1 1-.25 11.4 11.4 0 0 0 3.6.57 1 1 0 0 1 1 1V20a1 1 0 0 1-1 1A17 17 0 0 1 3 4a1 1 0 0 1 1-1h3.5a1 1 0 0 1 1 1c0 1.25.2 2.45.57 3.57a1 1 0 0 1-.25 1z"/></svg>(555) 614-3082</div>
    <div class="abs" style="left:250px;top:312px;color:#fff;font-size:7px;font-weight:600">www.dunmorelaw.com</div>
    <div class="abs logo" style="left:14px;top:306px;color:#fff"><span class="logo-mark"></span>Dunmore Law</div>
  </article>
</section>

<!-- ===== Design 2 – flat pair ===== -->
<section class="set set-flat" style="top:2220px">
  <article class="card front-two" style="left:80px;top:0">
    <div class="photo" role="img" aria-label="Attorney in a navy suit in front of an American flag" style="left:0;top:0;width:230px;height:340px;background:linear-gradient(120deg,#2a3f73 0%,#b73a3a 28%,#e9e6e2 45%,#4a5a78 70%,#1f2d4f 100%)"></div>
    <div class="abs" style="left:230px;top:0;width:280px;height:150px;background:var(--gold)"></div>
    <div class="abs headline" style="left:250px;top:28px;width:240px;font-size:22px;color:#fff">Serving People Injured in NY &amp; NJ</div>
    <div class="abs" style="left:230px;top:150px;width:280px;height:90px;background:#fff"></div>
    <div class="abs offer" style="left:250px;top:172px;width:240px;font-size:14px;color:var(--navy)">Free Consultation and<br>No Fee Unless We Recover Money</div>
    <div class="abs" style="left:230px;top:240px;width:280px;height:100px;background:var(--navy)"></div>
    <p class="abs small" style="left:250px;top:262px;width:140px;color:#fff">If you were injured in an accident, call us today for a free case review.</p>
    <div class="abs phone" style="left:402px;top:266px;color:#fff"><svg viewBox="0 0 24 24" fill="var(--gold)"><path d="M6.6 10.8a15 15 0 0 0 6.6 6.6l2.2-2.2a1 1 0 0 1 1-.25 11.4 11.4 0 0 0 3.6.57 1 1 0 0 1 1 1V20a1 1 0 0 1-1 1A17 17 0 0 1 3 4a1 1 0 0 1 1-1h3.5a1 1 0 0 1 1 1c0 1.25.2 2.45.57 3.57a1 1 0 0 1-.25 1z"/></svg>(555) 614-3082</div>
    <div class="abs" style="left:250px;top:312px;color:#fff;font-size:7px;font-weight:600">www.dunmorelaw.com</div>
    <div class="abs logo" style="left:14px;top:306px;color:#fff"><span class="logo-mark"></span>Dunmore Law</div>
  </article>
  <article class="card back-two" style="left:610px;top:0">
    <div class="photo" role="img" aria-label="Courthouse columns with a navy overlay" style="left:0;top:0;width:230px;height:340px;background:linear-gradient(180deg,#3b5c93 0%,#8da0bf 45%,#5d6f8e 100%)"></div>
    <div class="abs" style="left:0;top:0;width:230px;height:340px;background:linear-gradient(180deg,rgba(27,47,94,.85),rgba(27,47,94,.15) 55%,rgba(27,47,94,.05))"></div>
    <div class="abs" style="left:22px;top:50px;color:#fff">
      <div class="areas-title">Practice Areas</div>
      <ul class="areas"><li>Car Accidents</li><li>Motorcycle Accidents</li><li>Slip and Fall</li><li>Trip and Fall</li><li>Dog Bite Injuries</li><li>Pedestrian Accidents</li></ul>
    </div>
    <div class="abs" style="left:230px;top:0;width:280px;height:340px;background:linear-gradient(180deg,var(--blue-mid),var(--navy))"></div>
    <div class="abs tab" style="left:250px;top:22px;width:210px">Law Office of Walter Dunmore P.C.<br>New York</div>
    <div class="abs post-lines" style="left:260px;top:150px;width:220px;color:#fff"><span></span><span></span><span></span><span></span></div>
    <div class="ref-box" style="left:420px;top:300px;color:#fff"></div>
  </article>
</section>

<!-- ===== Design 3 – staged pair ===== -->
<section class="set set-staged" style="top:2560px">
  <article class="card back-three" style="left:130px;top:20px">
    <div class="abs" style="left:22px;top:26px;color:var(--navy)">
      <div class="areas-title">Practice Areas</div>
      <ul class="areas" style="color:var(--ink)"><li>Car Accidents</li><li>Motorcycle Accidents</li><li>Slip and Fall</li><li>Trip and Fall</li><li>Dog Bite Injuries</li><li>Staircase Injuries</li></ul>
    </div>
    <div class="photo" role="img" aria-label="Woman holding her ankle after a fall on a staircase" style="left:130px;top:70px;width:150px;height:150px;background:linear-gradient(150deg,#efeeec,#b9b7b4 60%,#7d7b78)"></div>
    <div class="abs" style="left:0;top:220px;width:280px;height:120px;background:var(--navy)"></div>
    <div class="abs" style="left:0;top:220px;width:280px;height:5px;background:var(--gold)"></div>
    <div class="abs" style="left:22px;top:250px;width:240px;color:#fff;font-weight:700;font-size:11px;line-height:1.25;text-transform:uppercase">Law Office of Walter Dunmore P.C. New York Personal Injury Attorneys</div>
    <div class="abs" style="left:300px;top:0;width:1px;height:340px;background:#d6dbe3"></div>
    <div class="stamp" style="left:452px;top:18px;color:var(--grey)"></div>
    <div class="abs post-lines" style="left:318px;top:150px;width:170px;color:var(--grey)"><span></span><span></span><span></span><span></span></div>
    <div class="ref-box" style="left:430px;top:302px;color:var(--grey)"></div>
  </article>
  <article class="card front-three" style="left:400px;top:300px">
    <div class="abs" style="left:0;top:0;width:510px;height:340px;background:var(--navy)"></div>
    <div class="photo" role="img" aria-label="Injured woman on the street and an attorney in a navy suit" style="left:150px;top:0;width:200px;height:340px;background:linear-gradient(100deg,#a9a9a6 0%,#d9d7d2 40%,#56637d 75%,#2b3757 100%)"></div>
    <div class="abs logo" style="left:18px;top:24px;color:#fff"><span class="logo-mark"></span>Dunmore Law</div>
    <div class="abs" style="left:0;top:80px;width:180px;height:130px;background:var(--gold)"></div>
    <div class="abs headline" style="left:16px;top:94px;width:160px;font-size:20px;color:#fff">Serving People Injured in NY &amp; NJ</div>
    <div class="abs phone" style="left:18px;top:250px;color:#fff"><svg viewBox="0 0 24 24" fill="var(--gold)"><path d="M6.6 10.8a15 15 0 0 0 6.6 6.6l2.2-2.2a1 1 0 0 1 1-.25 11.4 11.4 0 0 0 3.6.57 1 1 0 0 1 1 1V20a1 1 0 0 1-1 1A17 17 0 0 1 3 4a1 1 0 0 1 1-1h3.5a1 1 0 0 1 1 1c0 1.25.2 2.45.57 3.57a1 1 0 0 1-.25 1z"/></svg>(555) 614-3082</div>
    <div class="abs" style="left:18px;top:272px;color:#fff;font-size:7px;font-weight:600">www.dunmorelaw.com</div>
    <div class="abs offer" style="left:366px;top:170px;width:130px;font-size:13px;color:#fff">Free Consultation and No Fee Unless We Recover Money</div>
    <div class="abs" style="left:366px;top:244px;width:60px;height:3px;background:var(--gold)"></div>
    <p class="abs small" style="left:366px;top:256px;width:130px;color:#fff">If you were injured in an accident, call us today for a free case review.</p>
  </article>
</section>

<!-- ===== Design 3 – flat pair ===== -->
<section class="set set-flat" style="top:3440px">
  <article class="card front-three" style="left:80px;top:0">
    <div class="abs" style="left:0;top:0;width:510px;height:340px;background:var(--navy)"></div>
    <div class="photo" role="img" aria-label="Injured woman on the street and an attorney in a navy suit" style="left:150px;top:0;width:200px;height:340px;background:linear-gradient(100deg,#a9a9a6 0%,#d9d7d2 40%,#56637d 75%,#2b3757 100%)"></div>
    <div class="abs logo" style="left:18px;top:24px;color:#fff"><span class="logo-mark"></span>Dunmore Law</div>
    <div class="abs" style="left:0;top:80px;width:180px;height:130px;background:var(--gold)"></div>
    <div class="abs headline" style="left:16px;top:94px;width:160px;font-size:20px;color:#fff">Serving People Injured in NY &amp; NJ</div>
    <div class="abs phone" style="left:18px;top:250px;color:#fff"><svg viewBox="0 0 24 24" fill="var(--gold)"><path d="M6.6 10.8a15 15 0 0 0 6.6 6.6l2.2-2.2a1 1 0 0 1 1-.25 11.4 11.4 0 0 0 3.6.57 1 1 0 0 1 1 1V20a1 1 0 0 1-1 1A17 17 0 0 1 3 4a1 1 0 0 1 1-1h3.5a1 1 0 0 1 1 1c0 1.25.2 2.45.57 3.57a1 1 0 0 1-.25 1z"/></svg>(555) 614-3082</div>
    <div class="abs" style="left:18px;top:272px;color:#fff;font-size:7px;font-weight:600">www.dunmorelaw.com</div>
    <div class="abs offer" style="left:366px;top:170px;width:130px;font-size:13px;color:#fff">Free Consultation and No Fee Unless We Recover Money</div>
    <div class="abs" style="left:366px;top:244px;width:60px;height:3px;background:var(--gold)"></div>
    <p class="abs small" style="left:366px;top:256px;width:130px;color:#fff">If you were injured in an accident, call us today for a free case review.</p>
  </article>
  <article class="card back-three" style="left:610px;top:0">
    <div class="abs" style="left:22px;top:26px;color:var(--navy)">
      <div class="areas-title">Practice Areas</div>
      <ul class="areas" style="color:var(--ink)"><li>Car Accidents</li><li>Motorcycle Accidents</li><li>Slip and Fall</li><li>Trip and Fall</li><li>Dog Bite Injuries</li><li>Staircase Injuries</li></ul>
    </div>
    <div class="photo" role="img" aria-label="Woman holding her ankle after a fall on a staircase" style="left:130px;top:70px;width:150px;height:150px;background:linear-gradient(150deg,#efeeec,#b9b7b4 60%,#7d7b78)"></div>
    <div class="abs" style="left:0;top:220px;width:280px;height:120px;background:var(--navy)"></div>
    <div class="abs" style="left:0;top:220px;width:280px;height:5px;background:var(--gold)"></div>
    <div class="abs" style="left:22px;top:250px;width:240px;color:#fff;font-weight:700;font-size:11px;line-height:1.25;text-transform:uppercase">Law Office of Walter Dunmore P.C. New York Personal Injury Attorneys</div>
    <div class="abs" style="left:300px;top:0;width:1px;height:340px;background:#d6dbe3"></div>
    <div class="stamp" style="left:452px;top:18px;color:var(--grey)"></div>
    <div class="abs post-lines" style="left:318px;top:150px;width:170px;color:var(--grey)"><span></span><span></span><span></span><span></span></div>
    <div class="ref-box" style="left:430px;top:302px;color:var(--grey)"></div>
  </article>
</section>

</div>
</body>
</html>
```